Revise our Visual Graphic - CPA firm

We are a small specialty CPA firm that provides consulting services to companies in three areas: Information Security, Compliance & Attestation.

We need a tool to present our range of services and how they help our customers. We might use this on the website and when meeting face to face with clients to talk through what we do and how we can help.

I'm seeking a revised and updated graphic presentation image to explain our services. This graphic framework image will be one we can use on our website and use when we sell and explain our services to our clients. This graphic framework is meant to be a visual tool to make is easier to explain what we do to our clients.

We have a graphic that we like, but we don't LOVE IT yet. Your mission is you choose to accept it is to professionalize our graphic design. (see attached graphic)

The overall "environment" is represented by RISK, REGULATORY, REVENUE. These are the 3 reasons people would hire us. The bigger picture eco system.

The three overlapping circles show are three major service categories and inside the circles are lists of the specific services we can provide. We have overlapping circles to show that we can save them money and time if we provide more than one type of service.

The words on the dotted lines are what we commonly do on each project which is 3 things: IDENTIFY, EVALUATE, REPORT. These three things we do for all of our services so a faint circle with arrows or somehow showing a circular ongoing process would be good.

As you can see we are using one graphic to show many things and relationships.

The title of this graphic is "T5 Framework"

I look forward to your great ideas! Thanks.

Reason: Just to give a little more time after the weekend.

Target Market(s)

Presidents and Vice Presidents of small companies.

Industry/Entity Type

Graphic Design

Colors
faee3f
86cfc7
acd037
f68d4d

Requirements
Must have
• Be able to show this visual on one page of a website or PowerPoint presentation without scrolling down.

All of the written text on my draft example must be used and fit into the new design.
Nice to have
• When you design it think of how this can be used for both presentations, but also may be used on the website and people might click on different elements to learn more.

I picked some colors, but feel free to pick other colors. The only important thing to know is that the logo is black and yellow.

```html
<!DOCTYPE html>
<html lang="en">
<head>
<meta charset="utf-8">
<title>T5 Framework</title>
<link rel="stylesheet" href="https://fonts.googleapis.com/css2?family=Open+Sans:wght@600;700;800&family=Dosis:wght@600;700&display=swap">
<style>
  :root {
    --bg-light: #ffffff;
    --bg-mid: #b9cfcc;
    --bg-dark: #5d9a94;
    --ink: #231f20;
    --white: #ffffff;
    --blue: #29b6e8;
    --blue-deep: #1a9bd4;
    --green: #8dc63f;
    --green-deep: #74ad2f;
    --red: #ee1c25;
    --red-deep: #cf151d;
    --panel: #eef0f0;
    --hub: #e9e9e9;
  }
  html, body {
    margin: 0;
    padding: 0;
    width: 1200px;
    height: 900px;
    overflow: hidden;
  }
  .framework {
    width: 1200px;
    height: 900px;
    display: block;
    background: linear-gradient(125deg, var(--bg-light) 0%, var(--bg-mid) 45%, var(--bg-dark) 100%);
  }
  .title, .step-label {
    font-family: "Open Sans", Arial, sans-serif;
    font-weight: 700;
    fill: var(--ink);
  }
  .title { font-size: 21px; }
  .step-label { font-size: 21px; }
  .driver-label {
    font-family: "Dosis", "Arial Rounded MT Bold", sans-serif;
    font-weight: 700;
    font-size: 12.5px;
    fill: var(--white);
    letter-spacing: 0.3px;
  }
  .arc-label {
    font-family: "Dosis", "Arial Rounded MT Bold", sans-serif;
    font-weight: 700;
    font-size: 17px;
    fill: var(--white);
    letter-spacing: 0.6px;
  }
  .service-list {
    font-family: "Open Sans", Arial, sans-serif;
    font-weight: 700;
    font-size: 10.5px;
    fill: var(--white);
  }
  .hub-name {
    font-family: "Open Sans", Arial, sans-serif;
    font-weight: 700;
    font-size: 11.5px;
    fill: var(--ink);
  }
  .dots {
    stroke: var(--white);
    stroke-width: 5;
    stroke-linecap: round;
    stroke-dasharray: 0 8.5;
    fill: none;
  }
</style>
</head>
<body>
<svg class="framework" viewBox="0 0 1024 768" width="1200" height="900" xmlns="http://www.w3.org/2000/svg">
  <defs>
    <filter id="soft-shadow" x="-20%" y="-20%" width="140%" height="140%">
      <feDropShadow dx="4" dy="6" stdDeviation="7" flood-color="#1d3b38" flood-opacity="0.35"/>
    </filter>
    <linearGradient id="panel-fill" x1="0" y1="0" x2="1" y2="1">
      <stop offset="0" stop-color="#f6f7f7"/>
      <stop offset="1" stop-color="#e2e6e6"/>
    </linearGradient>
    <radialGradient id="hub-fill" cx="0.45" cy="0.4" r="0.7">
      <stop offset="0" stop-color="#ffffff"/>
      <stop offset="1" stop-color="#cfcfcf"/>
    </radialGradient>
    <path id="arc-red" d="M408,401 A140,140 0 0 1 596,401"/>
    <path id="arc-blue" d="M375,446 A140,140 0 0 0 478,643"/>
    <path id="arc-green" d="M526,643 A140,140 0 0 0 623,435"/>
  </defs>

  <text class="title" x="512" y="51" text-anchor="middle">T5 FRAMEWORK</text>

  <!-- environment triangle -->
  <polygon class="environment" points="506,185 200,643 820,643" fill="url(#panel-fill)" stroke="var(--white)" stroke-width="9" stroke-linejoin="round" filter="url(#soft-shadow)"/>

  <!-- process dotted paths -->
  <line class="dots" x1="210" y1="578" x2="458" y2="198"/>
  <line class="dots" x1="556" y1="196" x2="806" y2="578"/>
  <line class="dots" x1="258" y1="660" x2="760" y2="660"/>

  <text class="step-label" x="281" y="352" text-anchor="middle">IDENTIFY</text>
  <text class="step-label" x="737" y="348" text-anchor="middle">EVALUATE</text>
  <text class="step-label" x="498" y="698" text-anchor="middle">REPORT</text>

  <!-- service wheel -->
  <g class="service-wheel" filter="url(#soft-shadow)">
    <path class="segment-red" d="M502,505 L384,401 A157,157 0 0 1 620,401 Z" fill="var(--red)"/>
    <path class="segment-green" d="M502,505 L620,401 A157,157 0 0 1 502,662 Z" fill="var(--green)"/>
    <path class="segment-blue" d="M502,505 L502,662 A157,157 0 0 1 384,401 Z" fill="var(--blue)"/>
  </g>
  <path d="M502,505 L407,421 A127,127 0 0 1 597,421 Z" fill="var(--red-deep)"/>
  <path d="M502,505 L597,421 A127,127 0 0 1 502,632 Z" fill="var(--green-deep)"/>
  <path d="M502,505 L502,632 A127,127 0 0 1 407,421 Z" fill="var(--blue-deep)"/>

  <text class="arc-label"><textPath href="#arc-red" startOffset="50%" text-anchor="middle">INFORMATION SECURITY</textPath></text>
  <text class="arc-label"><textPath href="#arc-blue" startOffset="50%" text-anchor="middle">INFORMATION SECURITY</textPath></text>
  <text class="arc-label"><textPath href="#arc-green" startOffset="50%" text-anchor="middle">INFORMATION SECURITY</textPath></text>

  <text class="service-list" text-anchor="middle">
    <tspan x="502" y="386">ISO 27001</tspan>
    <tspan x="502" y="401">PCI-DSS</tspan>
    <tspan x="502" y="416">Penetration Test</tspan>
  </text>
  <text class="service-list" text-anchor="middle">
    <tspan x="434" y="480">CFPB</tspan>
    <tspan x="434" y="495">Readiness</tspan>
    <tspan x="434" y="510">FISMA</tspan>
    <tspan x="434" y="525">FedRamp</tspan>
    <tspan x="434" y="540">HITECH</tspan>
    <tspan x="434" y="555">HIPAA</tspan>
  </text>
  <text class="service-list" text-anchor="middle">
    <tspan x="562" y="496">SSAE 16</tspan>
    <tspan x="562" y="511">TrustMark</tspan>
    <tspan x="562" y="526">SOC 2</tspan>
  </text>

  <!-- hub -->
  <circle cx="502" cy="468" r="37" fill="var(--white)"/>
  <circle cx="502" cy="468" r="31" fill="url(#hub-fill)"/>
  <text class="hub-name" x="502" y="472" text-anchor="middle">Q-VERIS</text>

  <!-- drivers -->
  <g class="driver driver-regulatory" filter="url(#soft-shadow)">
    <circle cx="506" cy="148" r="60" fill="var(--blue)"/>
    <circle cx="506" cy="148" r="48" fill="var(--blue-deep)"/>
    <text class="driver-label" x="506" y="153" text-anchor="middle">REGULATORY</text>
  </g>
  <g class="driver driver-risk" filter="url(#soft-shadow)">
    <circle cx="185" cy="640" r="60" fill="var(--green)"/>
    <circle cx="185" cy="640" r="48" fill="var(--green-deep)"/>
    <text class="driver-label" x="185" y="645" text-anchor="middle">RISK</text>
  </g>
  <g class="driver driver-revenue" filter="url(#soft-shadow)">
    <circle cx="825" cy="640" r="60" fill="var(--red)"/>
    <circle cx="825" cy="640" r="48" fill="var(--red-deep)"/>
    <text class="driver-label" x="825" y="645" text-anchor="middle">REVENUE</text>
  </g>
</svg>
</body>
</html>
```